New Modern floristry business design

Hi, we are a new business based in Sydney called "velvet moss floristry"

With so many floristry's we need a good design that will set a great first impression.

A few descriptive words on how we envision velvet moss floristry:

-dynamic design
-minimal colour (colour can be used to enhance the design)
-black white grey (can include gold,silver,metallic shadowing)
Strong "VELVET MOSS" with a classy "FLORISTRY"
Bold with a touch of feminine

Industry/Entity Type

Business

Contact Information for Business Card

Velvet Moss Floristry,
Delphine Ruvek,
Velvetmossfloristry@quillmail.com.au

```html
<!DOCTYPE html>
<html lang="en">
<head>
<meta charset="utf-8">
<title>Velvet Moss Floristry — Business Cards</title>
<link rel="stylesheet" href="https://fonts.googleapis.com/css2?family=Kaushan+Script&family=Quicksand:wght@300;500&display=swap">
<style>
  :root {
    --page: #ffffff;
    --card-black: #1b1b1d;
    --card-charcoal: #333333;
    --gold: #e6d64a;
    --muted-grey: #8c8c8c;
    --white: #ffffff;
    --mark-grey: #6b6a66;
  }
  html, body {
    margin: 0;
    width: 1200px;
    height: 800px;
    overflow: hidden;
    background: var(--page);
  }
  .sheet {
    position: relative;
    width: 1200px;
    height: 800px;
  }
  .card {
    position: absolute;
    width: 476px;
    height: 280px;
    border-radius: 14px;
    overflow: hidden;
  }
  .card--black { background: var(--card-black); }
  .card--charcoal { background: var(--card-charcoal); }
  .card--top { top: 74px; }
  .card--bottom { top: 446px; }
  .card--back { left: 90px; }
  .card--front { left: 634px; }

  .contact {
    position: absolute;
    left: 0; right: 0;
    top: 98px;
    display: flex;
    flex-direction: column;
    align-items: center;
  }
  .contact__icon { width: 50px; height: 50px; }
  .contact__email {
    margin-top: 10px;
    font-family: "Quicksand", sans-serif;
    font-weight: 300;
    font-size: 21px;
    letter-spacing: 0.2px;
    white-space: nowrap;
  }
  .card--black .contact__email { color: var(--muted-grey); }
  .card--charcoal .contact__email { color: var(--white); }
  .card--black .contact__icon circle { fill: var(--muted-grey); }
  .card--charcoal .contact__icon circle { fill: var(--white); }

  .brand {
    position: absolute;
    left: 0; right: 0;
    top: 108px;
    display: flex;
    justify-content: center;
    align-items: center;
    gap: 12px;
  }
  .brand__dot {
    width: 40px; height: 40px;
    border-radius: 50%;
    background: var(--mark-grey);
    flex: none;
  }
  .brand__name {
    font-family: "Quicksand", sans-serif;
    font-weight: 500;
    font-size: 28px;
    white-space: nowrap;
  }
  .holder {
    position: absolute;
    left: 0; right: 0;
    top: 198px;
    text-align: center;
    font-family: "Kaushan Script", cursive;
    font-size: 21px;
  }
  .card--black .brand__name,
  .card--black .holder { color: var(--gold); }
  .card--charcoal .brand__name,
  .card--charcoal .holder { color: var(--white); }
</style>
</head>
<body>
<main class="sheet">

  <section class="card card--black card--top card--back">
    <div class="contact">
      <svg class="contact__icon" viewBox="0 0 50 50" aria-hidden="true">
        <circle cx="25" cy="25" r="24"/>
        <rect x="13" y="16" width="24" height="17" rx="1.5" fill="var(--card-black)"/>
        <path d="M13.5 17 L25 26 L36.5 17" fill="none" stroke="var(--muted-grey)" stroke-width="1.6"/>
      </svg>
      <div class="contact__email">Velvetmossfloristry@quillmail.com.au</div>
    </div>
  </section>

  <section class="card card--black card--top card--front">
    <div class="brand">
      <span class="brand__dot"></span>
      <span class="brand__name">Velvet Moss Floristry</span>
    </div>
    <div class="holder">Delphine Ruvek</div>
  </section>

  <section class="card card--charcoal card--bottom card--back">
    <div class="contact">
      <svg class="contact__icon" viewBox="0 0 50 50" aria-hidden="true">
        <circle cx="25" cy="25" r="24"/>
        <rect x="13" y="16" width="24" height="17" rx="1.5" fill="var(--card-charcoal)"/>
        <path d="M13.5 17 L25 26 L36.5 17" fill="none" stroke="var(--white)" stroke-width="1.6"/>
      </svg>
      <div class="contact__email">Velvetmossfloristry@quillmail.com.au</div>
    </div>
  </section>

  <section class="card card--charcoal card--bottom card--front">
    <div class="brand">
      <span class="brand__dot"></span>
      <span class="brand__name">Velvet Moss Floristry</span>
    </div>
    <div class="holder">Delphine Ruvek</div>
  </section>

</main>
</body>
</html>
```